WordPress Website for Pain Relief Clinic

I need a WordPress website designed for my laser pain relief clinic. It needs to be a professional, responsive design with 7 pages: Home, Why Choose Us, Treatable Conditions, Testimonials, FAQ, Franchising, Contact Us. Here is logo: https://files.brivoltcdn.com/media.t-w-e-n.com/sitebuilder/472/CalvexaLogoHighQuality.png

Target Market(s)

people with pain,elderly adults,injuries,soreness

Industry/Entity Type

Clinic

Number of Pages Required

5+ page

Colors
0792cd
85abd2

```html
<!DOCTYPE html>
<html lang="en">
<head>
<meta charset="utf-8">
<title>Calvexa Pain Treatment Center</title>
<link rel="stylesheet" href="https://fonts.googleapis.com/css2?family=Lato:wght@300;400;700;900&display=swap">
<style>
  :root {
    --page: #ffffff;
    --body: #1b1b1b;
    --brand: #0792cd;
    --brand-soft: #85abd2;
    --navy: #154a7e;
    --nav: #134a7c;
    --cta: #b71c1c;
    --text: #ffffff;
    --muted: #e6e6e6;
    --field: #e4e4e4;
    --submit: #9a8c8a;
  }
  * { box-sizing: border-box; margin: 0; padding: 0; }
  html, body { width: 1200px; height: 1000px; overflow: hidden; background: var(--page); }
  body { position: relative; font-family: "Lato", sans-serif; color: var(--text); }
  .site { position: absolute; left: 44px; top: 0; width: 1112px; height: 1000px; background: var(--body); overflow: hidden; }
  .abs { position: absolute; }

  .brand-name { left: 101px; top: 14px; font-size: 44px; font-weight: 900; color: var(--brand); letter-spacing: -1px; line-height: 1; }
  .search-box { left: 618px; top: 31px; width: 264px; height: 34px; background: #f0f0f0; border: 1px solid #ccc; }
  .search-box svg { position: absolute; left: 8px; top: 6px; }
  .search-btn { left: 888px; top: 31px; width: 89px; height: 34px; background: var(--brand); color: #fff; font-size: 14px; letter-spacing: 1px; text-align: center; line-height: 34px; }

  .hero-photo { left: 520px; top: 96px; width: 592px; height: 380px;
    background: radial-gradient(ellipse at 60% 40%, #c89a80 0%, #8a5f4e 22%, #1f4a6e 55%, rgba(27,27,27,0) 85%),
                linear-gradient(90deg, rgba(27,27,27,0) 0%, #12395c 60%, #0f3050 100%); }
  .hero-fade { left: 0; top: 96px; width: 1112px; height: 380px;
    background: linear-gradient(90deg, #1b1b1b 0%, rgba(27,27,27,0.9) 35%, rgba(27,27,27,0) 60%); }
  .hero-bottom { left: 0; top: 380px; width: 1112px; height: 100px; background: linear-gradient(180deg, rgba(27,27,27,0), #1b1b1b); }

  .main-nav { left: 0; top: 96px; width: 824px; height: 45px; background: var(--nav); display: flex; align-items: center; padding-left: 101px; font-size: 15px; }
  .main-nav a { color: var(--text); text-decoration: none; }
  .main-nav a.current { color: var(--brand); }
  .main-nav .sep { margin: 0 13px; }

  .hero-title { left: 98px; top: 170px; font-size: 76px; font-weight: 300; line-height: 78px; letter-spacing: 1px; }
  .hero-title strong { font-weight: 900; }
  .hero-sub { left: 98px; top: 327px; width: 402px; text-align: center; font-size: 19px; font-weight: 700; line-height: 24px; }
  .hero-sub .accent { color: var(--brand); }
  .cta { left: 103px; top: 393px; width: 392px; height: 40px; background: var(--cta); border-radius: 6px; text-align: center; line-height: 40px; font-size: 15px; font-weight: 700; }
  .arrow-left { left: 54px; top: 270px; }
  .arrow-right { left: 1034px; top: 270px; }

  .intro { left: 99px; top: 511px; width: 920px; font-size: 14px; line-height: 17px; color: var(--muted); }

  .thumb { width: 171px; height: 127px; }
  .t1 { left: 101px; top: 653px; background: linear-gradient(135deg, #b8aaa0, #f2ebe4); }
  .t2 { left: 280px; top: 653px; background: linear-gradient(135deg, #e8e4e0, #c98a64); }
  .t3 { left: 101px; top: 789px; background: linear-gradient(135deg, #8a6a4a, #e8e0d8); }
  .t4 { left: 280px; top: 789px; background: linear-gradient(135deg, #f4f0ec, #c0907a); }

  .signup { left: 469px; top: 653px; width: 291px; height: 219px; background: var(--navy); border-radius: 10px; }
  .signup h2 { position: absolute; left: 25px; top: 22px; font-size: 18px; font-weight: 400; }
  .field { position: absolute; left: 25px; width: 240px; height: 22px; background: var(--field); color: #444; font-size: 9px; line-height: 22px; padding-left: 8px; }
  .field::after { content: ""; position: absolute; right: 0; top: 0; width: 11px; height: 22px; border-left: 1px solid #bbb; }
  .submit { position: absolute; left: 25px; top: 177px; width: 105px; height: 22px; background: var(--submit); border-radius: 11px; font-size: 10px; font-weight: 700; text-align: center; line-height: 22px; }
  .signup-note { left: 470px; top: 885px; width: 300px; font-size: 14px; line-height: 17px; color: var(--muted); }

  .divider { left: 793px; top: 655px; width: 2px; height: 267px; background: #e8e8e8; }
  .contact { left: 821px; top: 650px; font-size: 15px; line-height: 19px; color: var(--muted); }
  .contact h3 { font-size: 20px; font-weight: 300; margin-bottom: 13px; color: #fff; }
  .contact h4 { font-size: 15px; font-weight: 700; margin: 38px 0 20px; color: #fff; }
  .contact .hours { font-size: 16px; font-weight: 700; color: #fff; }

  .site-footer { left: 0; top: 965px; width: 1112px; height: 35px; background: var(--brand); font-size: 14px; line-height: 33px; padding-left: 100px; }
  .social { position: absolute; top: 5px; width: 22px; height: 22px; border: 1.5px solid #fff; border-radius: 50%; }
</style>
</head>
<body>
<div class="site">
  <header>
    <div class="abs brand-name">Calvexa</div>
    <div class="abs search-box">
      <svg width="22" height="22" viewBox="0 0 22 22" fill="none" stroke="#888" stroke-width="2"><circle cx="9" cy="9" r="6"/><line x1="13.5" y1="13.5" x2="20" y2="20"/></svg>
    </div>
    <div class="abs search-btn">search</div>
  </header>

  <section class="hero">
    <div class="abs hero-photo" role="img" aria-label="Woman seen from behind holding her sore shoulder, glowing red at the neck"></div>
    <div class="abs hero-fade"></div>
    <div class="abs hero-bottom"></div>
    <nav class="abs main-nav">
      <a class="current" href="#">Home</a><span class="sep">|</span>
      <a href="#">Why Choose Us</a><span class="sep">|</span>
      <a href="#">Treatable Conditions</a><span class="sep">|</span>
      <a href="#">Testimonials</a><span class="sep">|</span>
      <a href="#">FAQ</a><span class="sep">|</span>
      <a href="#">Franchising</a><span class="sep">|</span>
      <a href="#">Contact Us</a>
    </nav>
    <h1 class="abs hero-title">SUFFERING<br>FROM <strong>PAIN</strong>?</h1>
    <p class="abs hero-sub">relive back pain, knee pain and shoulder pain using our <span class="accent">specialized laser treatment</span></p>
    <div class="abs cta">BOOK AN APPOINTMENT NOW</div>
    <svg class="abs arrow-left" width="26" height="44" viewBox="0 0 26 44" fill="none" stroke="#9aa" stroke-width="2"><polyline points="24,2 2,22 24,42"/></svg>
    <svg class="abs arrow-right" width="26" height="44" viewBox="0 0 26 44" fill="none" stroke="#9aa" stroke-width="2"><polyline points="2,2 24,22 2,42"/></svg>
  </section>

  <p class="abs intro">Calvexa Pain Treatment Center Lorem ipsum dolor sit amet, consectetur adipiscing elit, sed do eiusmod tempor incididunt ut labore et dolore magna aliqua. Ut enim ad minim veniam, quis nostrud exercitation ullamco laboris nisi ut aliquip ex ea commodo consequat. Duis aute irure dolor in reprehenderit in voluptate velit esse cillum dolore eu fugiat nulla pariatur. Excepteur sint occaecat cupidatat non proident, sunt in culpa qui officia deserunt mollit anim id est laborum.</p>

  <div class="abs thumb t1" role="img" aria-label="Older patient wearing goggles receiving laser treatment on the neck"></div>
  <div class="abs thumb t2" role="img" aria-label="Laser device applied to a patient's lower back"></div>
  <div class="abs thumb t3" role="img" aria-label="Laser device applied to a patient's elbow"></div>
  <div class="abs thumb t4" role="img" aria-label="Laser device applied to a patient's knee"></div>

  <form class="abs signup">
    <h2>Sign up for a FREE consultation</h2>
    <div class="field" style="top:64px">Name</div>
    <div class="field" style="top:101px">Email Address</div>
    <div class="field" style="top:139px">Country of Residence</div>
    <div class="submit">Submit</div>
  </form>
  <p class="abs signup-note">Sign up for our email newsletter and get a FREE consultation from our World Class Doctors!</p>

  <div class="abs divider"></div>
  <div class="abs contact">
    <h3>CALL US TODAY!</h3>
    <p>Tel: 555-014-2270</p>
    <p>E-mail: hello@calvexa-care.com</p>
    <h4>Operating Hours:</h4>
    <p>Weekdays</p>
    <p class="hours">8:00AM to 7:00PM</p>
    <p>Weekend</p>
    <p class="hours">8:00AM to 3:00PM</p>
  </div>

  <footer class="abs site-footer">
    Calvexa Pain Treatment Center <strong>© 2015</strong>
    <span class="social" style="left:920px"></span>
    <span class="social" style="left:953px"></span>
    <span class="social" style="left:987px"></span>
  </footer>
</div>
</body>
</html>
```